Criação de Papelaria Profissional para Construção & Engenharia
" Gerenciando projetos de construções de lojas tipo magazine e outros tipos de imóveis comerciais. "

```html
<!DOCTYPE html>
<html lang="pt-BR">
<head>
<meta charset="utf-8">
<title>MODULA – Envelope</title>
<link rel="stylesheet" href="https://fonts.googleapis.com/css2?family=Montserrat:wght@500;700;800&display=swap">
<style>
  :root {
    --bg: #e4e4e4;
    --paper: #ffffff;
    --red: #e3241b;
    --red-dark: #c81a13;
    --ink: #5a5a5a;
    --muted: #8a8a8a;
  }
  * { box-sizing: border-box; margin: 0; padding: 0; }
  html, body { width: 1200px; height: 1200px; overflow: hidden; }
  body {
    background: var(--bg);
    font-family: "Montserrat", Arial, sans-serif;
    position: relative;
  }
  .envelope {
    position: absolute;
    top: 230px;
    width: 500px;
    height: 720px;
    box-shadow: 0 6px 18px rgba(0,0,0,0.12);
  }
  .envelope--front { left: 70px; background: var(--paper); }
  .envelope--back { left: 630px; background: var(--red); }

  .flap { position: absolute; top: 0; left: 0; width: 500px; height: 56px; display: block; }

  .brand {
    position: absolute;
    left: 0; right: 0;
    text-align: center;
  }
  .envelope--front .brand { top: 170px; }
  .envelope--back .brand { bottom: 110px; }
  .brand__name {
    display: inline-flex;
    align-items: center;
    gap: 12px;
    font-weight: 800;
    font-size: 46px;
    letter-spacing: 2px;
    line-height: 1;
  }
  .brand__dot { width: 18px; height: 18px; background: var(--red); display: inline-block; }
  .brand__tagline {
    margin-top: 8px;
    font-weight: 700;
    font-size: 11px;
    letter-spacing: 3px;
    text-transform: uppercase;
  }
  .envelope--front .brand__name { color: var(--ink); }
  .envelope--front .brand__tagline { color: var(--red); }
  .envelope--back .brand__name,
  .envelope--back .brand__tagline { color: var(--paper); }
  .envelope--back .brand__dot { background: var(--paper); }

  .contact {
    position: absolute;
    left: 34px;
    bottom: 46px;
    display: flex;
    gap: 44px;
    font-size: 9px;
    font-weight: 500;
    color: var(--muted);
  }
  .contact__col { display: flex; flex-direction: column; gap: 9px; }
  .contact__item { display: flex; align-items: flex-start; gap: 6px; line-height: 1.35; }
  .contact__icon { width: 11px; height: 11px; flex: none; }
</style>
</head>
<body>

  <section class="envelope envelope--front" aria-label="Frente do envelope">
    <svg class="flap" viewBox="0 0 500 56" aria-hidden="true">
      <path d="M0 0 H500 V56 H470 L440 12 H60 L30 56 H0 Z" fill="var(--red)"/>
    </svg>

    <div class="brand">
      <div class="brand__name"><span class="brand__dot"></span>MODULA</div>
      <div class="brand__tagline">Construções e Reformas</div>
    </div>

    <div class="contact">
      <div class="contact__col">
        <div class="contact__item">
          <svg class="contact__icon" viewBox="0 0 12 12"><circle cx="6" cy="6" r="6" fill="var(--red)"/><path d="M4 3.2 L5 3 L5.6 4.6 L5 5.1 Q5.6 6.4 6.9 7 L7.4 6.4 L9 7 L8.8 8 Q5 8.6 3.9 4.2 Z" fill="#fff"/></svg>
          <span>(11) 4000-2000</span>
        </div>
        <div class="contact__item">
          <svg class="contact__icon" viewBox="0 0 12 12"><circle cx="6" cy="6" r="6" fill="var(--red)"/><rect x="3" y="4" width="6" height="4" fill="none" stroke="#fff" stroke-width="0.8"/><path d="M3 4 L6 6.3 L9 4" fill="none" stroke="#fff" stroke-width="0.8"/></svg>
          <span>contato@modulaobras.com.br</span>
        </div>
      </div>
      <div class="contact__col">
        <div class="contact__item">
          <svg class="contact__icon" viewBox="0 0 12 12"><circle cx="6" cy="6" r="6" fill="var(--red)"/><circle cx="6" cy="6" r="3" fill="none" stroke="#fff" stroke-width="0.8"/><path d="M3 6 H9 M6 3 V9" stroke="#fff" stroke-width="0.6"/></svg>
          <span>www.modulaobras.com.br</span>
        </div>
        <div class="contact__item">
          <svg class="contact__icon" viewBox="0 0 12 12"><circle cx="6" cy="6" r="6" fill="var(--red)"/><path d="M6 9.2 L4 6 A2.3 2.3 0 1 1 8 6 Z" fill="#fff"/><circle cx="6" cy="5" r="0.8" fill="var(--red)"/></svg>
          <span>Rua das Obras, 120 - Centro<br>São Paulo - SP, 01000-000</span>
        </div>
      </div>
    </div>
  </section>

  <section class="envelope envelope--back" aria-label="Verso do envelope">
    <div class="brand">
      <div class="brand__name"><span class="brand__dot"></span>MODULA</div>
      <div class="brand__tagline">Construções e Reformas</div>
    </div>
  </section>

</body>
</html>
```